Web page update/ Create new non flash site

I have a flash web page, created by my ex girlfriend through some kind of web design service. I want to take all of the information that I have on the page and put it together in a similar manner on a non-flash page.I want to add a lot of pictures, update the logo to the one i had made on pixel bazaar and reword a few things to reflect the the direction my business has gone in, in the past couple years since I made the site.. I also can't figure out why when people e-mail me from my page, I get the e-mail but no message, happens all the time and makes me think I'm losing business. My main problem is that I don't know what service was used in the past to create this page or what information someone would need to be able to work on it more. I also have another domain name that I want connected to it. the existing web page is at www.quillbyconstruction.net

Target Market(s)

I originally made this web page thinking that i was going to be in the remodeling business, but the majority of the work i get is for high end commercial and residential millwork and carpentry installations. I mainly will be advertising to other general contractors, but I want to keep the same feel that it has now, how it is mainly talking to homeowners that are thinking about hiring me to do some sort of project for them.

Industry/Entity Type

Business

Requirements
Must have
• Portfolio page needs to be updated to have LOTS more pictures and have them in an organized manner where it's easy to navigate through them. My other main thing is that I want to keep the same look and feel that it has with the nice woodgrain background, user friendly layout of links, etc.

```html
<!DOCTYPE html>
<html lang="en">
<head>
<meta charset="utf-8">
<title>Quillby Construction — Building &amp; Renovation</title>
<link href="https://fonts.googleapis.com/css2?family=Source+Sans+3:wght@400;600&display=swap" rel="stylesheet">
<style>
  :root {
    --orange: #e0622a;
    --text: #444;
    --dash: #d6d6d6;
    --nav-top: #b4cad6;
    --nav-bottom: #85a6b8;
    --footer: #86aabf;
    --social: #3f6f8f;
    --white: #fff;
  }
  * { box-sizing: border-box; margin: 0; padding: 0; }
  html, body { width: 1156px; height: 1200px; overflow: hidden; }
  body {
    position: relative;
    background: var(--white);
    font-family: "Source Sans 3", "Myriad Pro", sans-serif;
    color: var(--text);
  }
  .abs { position: absolute; }
  h2 { font-weight: 400; }
  .header-band {
    left: 0; top: 0; width: 1156px; height: 103px;
    background: linear-gradient(#e4ecf1, #f6f9fb 70%, #fff);
  }
  .brand { left: 158px; top: 20px; }
  .brand-name { font-size: 27px; color: var(--orange); line-height: 1.1; }
  .brand-tag { font-size: 15px; color: #666; letter-spacing: 1px; margin-top: 1px; }
  .search {
    left: 777px; top: 36px; width: 223px; height: 27px;
    border: 1px solid #b9c9d3; border-radius: 3px; background: #fff;
    font-size: 12px; color: #888; padding: 6px 8px;
  }
  .search svg { position: absolute; right: 8px; top: 6px; }
  .nav {
    left: 401px; top: 82px; width: 598px; height: 30px; display: flex;
    background: linear-gradient(var(--nav-top), var(--nav-bottom));
    box-shadow: 0 3px 4px rgba(0,0,0,.25);
  }
  .nav a {
    flex: 1; text-align: center; line-height: 30px; font-size: 12px;
    color: #1f2f3a; text-decoration: none; border-right: 1px solid #6d8fa2;
  }
  .nav a:last-child { border-right: 0; }
  .slider {
    left: 164px; top: 137px; width: 489px; height: 334px; background: #fff;
    box-shadow: 0 1px 6px rgba(0,0,0,.3); padding: 8px;
  }
  .slide-photo {
    width: 100%; height: 100%;
    background: linear-gradient(172deg, #f1efea 0%, #e4dfd4 28%, #d6d0c4 40%, #8e8275 52%, #5d5147 60%, #2f2a26 72%, #4b4540 86%, #7a736a 100%);
  }
  .dots { position: absolute; right: 22px; bottom: 20px; display: flex; gap: 4px; }
  .dots span { width: 11px; height: 11px; border-radius: 50%; background: #fff; }
  .dots span.on { background: var(--orange); border: 2px solid #fff; }
  .box { border: 1px dashed var(--dash); background: #fff; }
  .box-title {
    position: absolute; left: 15px; right: 15px; font-size: 18px; color: var(--orange);
    border-bottom: 1px dotted #9fb3bf; padding-bottom: 6px;
  }
  .gallery { left: 673px; top: 137px; width: 322px; height: 178px; }
  .gallery .box-title { top: 12px; }
  .arrows { position: absolute; right: 12px; top: 19px; display: flex; gap: 6px; }
  .gallery-photo {
    position: absolute; left: 18px; top: 60px; width: 289px; height: 96px;
    background: linear-gradient(90deg, #4e3a2a 0%, #7a4f2e 20%, #8e5a32 45%, #6e4429 62%, #d9d6cc 72%, #bfbcb2 84%, #2b2826 92%, #1e1c1b 100%);
    box-shadow: 0 6px 6px -3px rgba(0,0,0,.35);
  }
  .contact { left: 673px; top: 325px; width: 322px; height: 148px; }
  .contact .box-title { top: 12px; }
  .contact-line {
    position: absolute; left: 20px; font-size: 18px; line-height: 22px; color: var(--orange);
    display: flex; align-items: center; gap: 10px;
  }
  .welcome {
    left: 163px; top: 489px; width: 832px; height: 177px; border: 1px solid #ddd;
    background: linear-gradient(#fff, #f0f0f0);
  }
  .welcome .box-title { top: 14px; left: 18px; right: 26px; }
  .copy { position: absolute; font-size: 11.5px; line-height: 19.5px; color: var(--text); text-align: justify; }
  .welcome .copy { left: 20px; top: 67px; width: 520px; }
  .welcome-photo {
    position: absolute; left: 570px; top: 63px; width: 240px; height: 95px;
    background: linear-gradient(180deg, #e9e4d9 0%, #cfc8bb 14%, #8a7f72 26%, #5f574e 40%, #b07544 55%, #9a5f30 75%, #b7793f 100%);
  }
  .why { left: 164px; top: 677px; width: 542px; height: 171px; }
  .why .box-title { top: 14px; }
  .why .copy { left: 18px; top: 55px; width: 506px; }
  .services { left: 716px; top: 677px; width: 279px; height: 171px; }
  .services .box-title { top: 12px; }
  .services .copy { left: 13px; top: 55px; width: 251px; hyphens: auto; }
  .read-more { position: absolute; right: 14px; bottom: 11px; font-size: 12px; color: var(--orange); }
  .portfolio-title { left: 165px; top: 863px; font-size: 17px; color: var(--orange); }
  .portfolio-arrows { left: 962px; top: 872px; display: flex; gap: 6px; }
  .footer { left: 0; top: 928px; width: 1156px; height: 272px; background: var(--footer); }
  .thumb {
    top: 897px; width: 196px; height: 80px; background: #fff; padding: 3px;
    box-shadow: 0 4px 5px rgba(0,0,0,.25);
  }
  .thumb div { width: 100%; height: 100%; }
  .map {
    left: 164px; top: 1003px; width: 314px; height: 172px;
    background: linear-gradient(160deg, #dfe7ef 0%, #f0dcd2 22%, #efd7cb 45%, #e9ded6 58%, #b7cfe6 75%, #a7c1dc 100%);
    box-shadow: 0 2px 4px rgba(0,0,0,.3);
  }
  .follow { right: 125px; top: 1014px; font-size: 17px; color: #fff; }
  .social { right: 127px; top: 1054px; display: flex; gap: 7px; }
  .social span { width: 21px; height: 21px; border-radius: 2px; background: var(--social); }
  .footer-nav { right: 125px; top: 1140px; font-size: 11.5px; color: #fff; }
  .footer-nav span { margin: 0 6px; }
  .copyright { right: 125px; top: 1162px; font-size: 11.5px; color: #fff; }
</style>
</head>
<body>
  <div class="abs header-band"></div>

  <div class="abs brand">
    <div class="brand-name">Quillby Construction</div>
    <div class="brand-tag">building &amp; renovation company</div>
  </div>

  <div class="abs search">Search
    <svg width="13" height="13" viewBox="0 0 13 13"><circle cx="5" cy="5" r="3.6" fill="none" stroke="#8a9aa5" stroke-width="1.6"/><line x1="7.6" y1="7.6" x2="12" y2="12" stroke="#8a9aa5" stroke-width="2"/></svg>
  </div>

  <nav class="abs nav">
    <a href="#">Home</a><a href="#">About Us</a><a href="#">Services</a><a href="#">Portfolio</a><a href="#">Process</a><a href="#">Contact Us</a>
  </nav>

  <div class="abs slider">
    <div class="slide-photo" role="img" aria-label="Renovated kitchen with white cabinets, stainless refrigerator and granite island"></div>
    <div class="dots"><span></span><span></span><span class="on"></span><span></span><span></span><span></span></div>
  </div>

  <section class="abs box gallery">
    <h2 class="box-title">Photo Gallery</h2>
    <div class="arrows">
      <svg width="9" height="14" viewBox="0 0 9 14"><path d="M7 1 L2 7 L7 13" fill="none" stroke="#222" stroke-width="2.4"/></svg>
      <svg width="9" height="14" viewBox="0 0 9 14"><path d="M2 1 L7 7 L2 13" fill="none" stroke="#e0622a" stroke-width="2.4"/></svg>
    </div>
    <div class="gallery-photo" role="img" aria-label="Kitchen with wood cabinets and a window"></div>
  </section>

  <section class="abs box contact">
    <h2 class="box-title">Contact Us</h2>
    <div class="contact-line" style="top:61px">
      <svg width="20" height="16" viewBox="0 0 20 16"><path d="M1 5 Q10 -1 19 5 L16 7 L13 5 L7 5 L4 7 Z" fill="#222"/><rect x="4" y="8" width="12" height="7" rx="1" fill="#222"/><circle cx="10" cy="11.5" r="2" fill="#fff"/></svg>
      <span>: 555.014.7720</span>
    </div>
    <div class="contact-line" style="top:97px">
      <svg width="20" height="16" viewBox="0 0 20 16"><path d="M1 6 L10 1 L19 6 L19 15 L1 15 Z" fill="#222"/><path d="M1 6 L10 11 L19 6" fill="none" stroke="#fff" stroke-width="1.3"/></svg>
      <span>: info@quillbyconstruction.net</span>
    </div>
  </section>

  <section class="abs welcome">
    <h2 class="box-title">Welcome to Our Site</h2>
    <p class="copy">Welcomet to Quillby Construction, a locally owned and operated residential construction company serving the greater New Orleans area. We Specialize in all forms of home remodeling, renovations and custome carpentry. No matter how big or small you next project is , you need not look further, Quillby Construction is here to accommodate your needs and surpass your expectations.</p>
    <div class="welcome-photo" role="img" aria-label="Kitchen counter with granite top and wood cabinets"></div>
  </section>

  <section class="abs box why">
    <h2 class="box-title">Why Choose Quillby Construction?</h2>
    <p class="copy">100% Customer satisfaction is what we strive for and achieve daily at Quillby Construction. we do not accept any projects as complete until our csutomeris completely satisfied with the wrok performed. Our building team has serviced high end clientele in all of the most prestigious areas of our great city and we are not until our csutomeris completely satisfied with the wrok performed. Our building team has serviced high end clientele in all of the most prestigious areas of our great city and we are not....</p>
  </section>

  <section class="abs box services">
    <h2 class="box-title">Services</h2>
    <p class="copy">If you can dream, it we can build it. Quillby Construction has its roots in home renovations, remodeling, additions, and custome carpentry. Our building team has serviced high end clientele in all of the most prestigious areas ofo ur ....</p>
    <a class="read-more">read more</a>
  </section>

  <div class="abs footer"></div>

  <h2 class="abs portfolio-title">Our Portfolio</h2>
  <div class="abs portfolio-arrows">
    <svg width="9" height="14" viewBox="0 0 9 14"><path d="M7 1 L2 7 L7 13" fill="none" stroke="#222" stroke-width="2.4"/></svg>
    <svg width="9" height="14" viewBox="0 0 9 14"><path d="M2 1 L7 7 L2 13" fill="none" stroke="#e0622a" stroke-width="2.4"/></svg>
  </div>

  <div class="abs thumb" style="left:165px"><div role="img" aria-label="Hallway with electrical panel" style="background:linear-gradient(90deg,#bdbcb8 0%,#d8d7d3 25%,#8f8a84 42%,#b4453c 50%,#8f8a84 58%,#d3d2ce 78%,#e4e3df 100%)"></div></div>
  <div class="abs thumb" style="left:376px"><div role="img" aria-label="House exterior with porch" style="background:linear-gradient(180deg,#7f9a6c 0%,#a7b59a 18%,#8a7a6c 35%,#c4c0b6 55%,#e7e5df 72%,#8b877d 100%)"></div></div>
  <div class="abs thumb" style="left:588px"><div role="img" aria-label="Freshly painted interior wall" style="background:linear-gradient(100deg,#ccc7bb 0%,#e2ded4 30%,#b9b4a6 52%,#cdd0bd 70%,#b8bca9 100%)"></div></div>
  <div class="abs thumb" style="left:798px"><div role="img" aria-label="Interior with wood cabinets and pendant light" style="background:linear-gradient(90deg,#b19c7c 0%,#e1d4bb 25%,#d8c7a4 42%,#7d5734 58%,#a06d3e 68%,#d8cbb2 85%,#6e4b2e 100%)"></div></div>

  <div class="abs map" role="img" aria-label="Map of North America showing the service area"></div>

  <div class="abs follow">Follow Us On</div>
  <div class="abs social" aria-label="Social links">
    <span></span><span></span><span></span><span></span>
  </div>

  <div class="abs footer-nav">Home<span>|</span>About Us<span>|</span>Services<span>|</span>Portfolio<span>|</span>Process<span>|</span>Contact Us</div>
  <div class="abs copyright">Copyrights @ 2012 All Rights Reserved</div>
</body>
</html>
```